Your new Home.

below is a lot of info so you can read and understand what I do I think it's important for the creator to know as much as possible so you can creatively decide what would work in a flyer. I want it to be edgy, modern, or very aggressive. I am very loud and proud we don't want to be like everyone else. Our slogan Is "Where Craftsmen Come to Reach the Summit" as every one in my business calls themselves professionals and being a master to me means the best at what you do. which we are. my company colors are Gold Maroon Black and grey and whit. I do like having lightning strikes and hail incorperated. We Do Have Promotions and coupons and referals we pay out on. below this is a bunch of info to understand what I do. I need a flyer that is informative about my company. That informs customers what we want to do. We are a company with over 30 years combined experience Myself 13 yrs experience. We are a Storm Damage Specialist Restoration General Contractor Company. We provide a service the helps insure homeowners not only can we provide the correct perferred method of repairs according to today's industry standards rules and regulations. but we know what is your responsibility as a homeowner, and what the responsibility of your insurer is according to The governing municipalities not only by the city and state, but according to States Insurance Departments That govern what Insurance carriers must do. We don't let big conglomerate companies profiting off thousands of homeowners constantly paying in with their raising premiums each year. We use the Guidelines set by the insurance commissioners office to make sure that carriers are approving and paying for more than just minimums. Carriers constantly state to homeowners and contractors that their company policies don't allow things especially when it comes to paying for full roof replacements, replacing all your siding on the entire home if its discontinued. Or replacing all gutters ect. Carriers constantly are coming in only approving and paying for minor repairs And doing partial roof replacements, patching in siding replacing 1 and 2 peices here and their sections of fascia and gutters ect. we are tired of Carriers using their tactics of Denying claims, defering responsibility, defending them self's . Who's left to defend the homeowners? Who's knows the right questions to ask, and in what order and when to ask them. We Do. That's because for over a decade We have perfected the process of Working with hundred of different carriers. By already having major success on over a couple thousand Storm Damage claims . in more than a decade. Every last one of the claims we have worked on. Our goal was to maximize each claim to complete repairs restoring homeowners damaged properties to their original condition as they were prior to their loss. We can't get carriers to do anything they are not obligated to do. We have have to document and and present any and all damages we find. Then present it in a way to a carrier to where it can't be denied stating it doesn't meet certan criteria's, or deferred that its not storm damage that it was caused by a non covered peril, or defend that they are their to take care of you, and we are just trying to make money off of them regardless of actual responsibility. We can navigate through this process where we are the ones taking all the risks and doing all the leg work. Our Time is very valuable. We can only be as effective as our customers allow. Meaning A lot of times carriers will try to divide and conquer. Meaning they want to cause doubt in our abilities, or paint a pictured of alternative Motives That aren't in your best intrest. Carriers know their contracts are with the insured not the Contractors . That they don't have to answer to us
That's why its very important to us to set the tone early on. We are here to make money by performing excellent work restoring your property from storm damage. Ask your self , if we sign homeowners up for us to be the Contractor of choice to repair all approved works, and we only make money off of works completed than wouldn't we want to get you as much work approved for us to do. Leaving the homeowner and the contractor us having the same goal, however carriers dont want that because they are the ones having to pay for it back. They don't want to pay out huge portions they have accumulated from all your yearly premiums. All our works have to be approved by the carriers no carrier is going to pay thousands to their policy holders unless they have to. You are kidding yourself if you don't think they aren't saving millions by not paying out when they are legally bond to. You entered a bi lateral contract with them that you would give them x amount of dollars for a service they would provide if certain listed perils occurred while your insurance was binded / in affect. We know what works and what doesn't. In the end we also don't set the prices we use a 3rd party system that all the carriers use That is a automated computer system that populates the current fair market value of all materials amd labors. Know as the Replacement Cost Value. So if we don't make the rule, or set the prices, and we do all our works upfront with no down payment. Theirs no way a carrier can when a argument that we are doing anything other than working for you to create as much work for us that results in your property Being restored to its original condition at the same time it is restoring thousands of dollars of value back into your. home. Leaving you most prized financial investment protected. Our goals are t ok perform the best quality workmanship and keeping homeowners out of pocket cost to not exceed their set deductibles. If your cost is the same regardless you know when you file a claim you want everything that would be related to storm damaged documented and restored and paid for, and that's what we want because that's what we do for a living, and we want to be the best at it.

explaining the proccess.

We schedual a free no obligation gable crest property damage assesment/ inspection, what that intales is A roof inspection of all roof surfaces on property and a exterior inspection f all structures on the property Dwelling Detacjed Garages Barns, Shops, Well Houses and more. And finally interior inspections as well. Looking for water damage to ceilings and walls and floors.

Once we have photo documented all the damages notated during inspection, a gable crest will then sit down and go over all of them and show you pictures we took of those damages and explain why they we believe they should be paid for by your carrier as a covered peril on you homeowners policy. All with you only paying a
deductible that you chose when you started the policy. We will then use a storm Damage app to populate your best storm Date of Loss That best helps your scenario to get all damages paid for. once we have shown you the damages and explained them to you. we will give you a contingency contract that is based off of us getting your insurance company you approve and pay for them. if we can't get your project approved you don't owe us a dime for all that time we spent inspecting documenting and calling in your claim and meeting your insurance scheduled adjuster. As this is how we make a living is winding homeowners with storm related damage. so once you have decided to see what we can do for you we file your claim with you. Then the adjuster assigned will reach out to you usually within 1 to 10 business day most likely within the 1st 72 business hours. They will schedule a time to come do a inspection, which we ask you to contact us and share that information as this us a very crucial part to getting the right things documented to that adjuster with statements that would would contribute to the adjuster having to approve the documented damages t ok be restored Once the adjuster complete the inspection, he submits his estimate written on a computer system that we also use meaning neither of us set the price we are only entering apple for apples aka same like kind and value to be removed and replaced. price is bases off of you zipcode and month where and when the works were privided/ incurred . Leaving you the homeowner only responsible for your deductible. Was you receive your estimate we will go over all approves line items with you and schedule them with you to meat you time line of what you have going on in your life. we can cater to all needs. We are financially set to do the works as fast as you would like or hold off until a certain time. That doing said through this entire process we do not request any down payments amd will be able to take the financial risks of completing the works 1st so you are never in a position to where yo iij have paid any moneys wiring about what the work will look like or when it will get done. Once we have finished all approved scope of works. We send off to them the final invoice stating all works have been completed and they release the rest of the funds allowed for those works. we are a 1 stop shop that will handle a those types of repairs. From roofing siding fascia soffit aluminum wraps garage doors drywall repair and painting amd more.

Target Market(s)

Home Owners, Useually 25 years old at least to 80 year olds. Most will be 30-50

Industry/Entity Type

Construction

Colors

Designer to choose colors to be used in the design.

Requirements
Must have
• My Company Name, My Logo that you can find On my Chatter web or web site fd- Gable Crest Builders Inc. www.gablecrestbuilding.example
• My Slogan
• Where Craftsmen Reach the Summit
• Contact info phone (555)382-6047
Nice to have
• Hail, and wind images Beautiful homes, disasters. Lightning striking hail falling SEVERE wind. I LOVE COMEDY. so any thing that is catchy or funny. Like Not a Shingle Mistake. as are number 1 thing we do is R&R Roofing
Should not have
• My Name,

```html
<!DOCTYPE html>
<html lang="en">
<head>
<meta charset="utf-8">
<title>Gable Crest Builders Flyers</title>
<link rel="stylesheet" href="https://fonts.googleapis.com/css2?family=Oswald:wght@600;700&family=Montserrat:wght@400;600;700&family=Open+Sans:wght@400;600&display=swap">
<style>
:root{
  --maroon:#5a0b1e;
  --maroon-deep:#3f0714;
  --gold:#c9a646;
  --ink:#222;
  --paper:#ffffff;
  --stage:#2e2e2e;
  --grey:#8a8a8a;
}
*{box-sizing:border-box;margin:0;padding:0}
html,body{width:1200px;height:800px;overflow:hidden}
body{background:var(--stage);position:relative;font-family:"Open Sans",sans-serif;color:var(--ink)}
.flyer{position:absolute;top:76px;width:500px;height:648px;background:var(--paper);overflow:hidden}
.flyer--front{left:50px}
.flyer--back{left:650px;background:var(--maroon)}
.abs{position:absolute}

/* front */
.hero-photo{left:0;top:0;width:500px;height:300px;background:linear-gradient(135deg,#3d56b8 0%,#6b7ad0 35%,#c98a3c 65%,#e0a04a 100%)}
.title-panel{left:0;top:250px;width:300px;height:155px;background:var(--maroon);border-top-right-radius:26px;padding:28px 18px 0 26px;color:var(--paper)}
.title-main{font-family:"Oswald",sans-serif;font-weight:700;font-size:34px;line-height:1;letter-spacing:.5px}
.title-sub{font-family:"Oswald",sans-serif;font-weight:700;font-size:28px;letter-spacing:8px;line-height:1.15}
.slogan{font-family:"Montserrat",sans-serif;font-size:9.5px;letter-spacing:1px;margin-top:6px}
.logo-oval{left:322px;top:120px;width:150px;height:180px;border-radius:50%;background:var(--paper);border:4px solid var(--maroon);display:flex;align-items:center;justify-content:center;text-align:center;padding:0 18px}
.logo-name{font-family:"Montserrat",sans-serif;font-weight:700;font-size:14px;color:var(--maroon);line-height:1.3}
.bar{background:var(--maroon);color:var(--paper);font-family:"Montserrat",sans-serif;font-weight:700;font-size:10px;letter-spacing:.5px;padding:5px 10px}
.why-bar{left:318px;top:312px;width:172px}
.why-text{left:320px;top:338px;width:168px;font-size:7.4px;line-height:1.45}
.services-bar{left:318px;top:398px;width:172px}
.services{left:326px;top:428px;list-style:none}
.services li{display:flex;align-items:center;gap:9px;height:27px;font-size:8px}
.services svg{width:18px;height:18px;flex:none}
.about{left:24px;top:420px;width:280px}
.about h2{font-family:"Montserrat",sans-serif;font-weight:600;font-size:14px;letter-spacing:3px;margin-bottom:6px}
.about p{font-size:7.4px;line-height:1.45;margin-bottom:6px}
.divider{left:312px;top:398px;width:1px;height:200px;background:var(--maroon)}

.footer{left:0;bottom:0;width:500px;height:54px;background:var(--maroon);color:var(--paper)}
.footer-cta{left:0;top:8px;width:380px;text-align:center;font-family:"Montserrat",sans-serif;font-size:11px}
.footer-cta b{font-weight:700}
.footer-rule{left:70px;top:26px;width:240px;height:1px;background:rgba(255,255,255,.6)}
.footer-line{left:22px;top:32px;font-family:"Montserrat",sans-serif;font-size:9.5px;letter-spacing:2px;display:flex;gap:14px;align-items:center;white-space:nowrap}
.footer-line svg{width:11px;height:11px;vertical-align:-1px;margin-right:5px}
.creds{left:392px;top:6px;width:100px;font-family:"Montserrat",sans-serif;font-size:7.5px;font-weight:600;letter-spacing:1px;line-height:1.25}
.badge{display:inline-block;width:12px;height:16px;background:var(--paper);border-radius:2px;position:absolute;left:74px;top:2px}
.social{margin-top:4px;font-size:7px;font-weight:400;letter-spacing:.5px}

/* back */
.adv-box{left:12px;top:11px;width:208px;height:151px;border:1.5px solid var(--paper);border-top-right-radius:34px;padding:9px 10px 0 12px;color:var(--paper);font-family:"Montserrat",sans-serif}
.adv-title{font-weight:700;font-size:10px;letter-spacing:2.5px;white-space:nowrap;padding-bottom:5px;border-bottom:1px solid var(--paper);width:150px;margin-bottom:6px}
.adv-list{list-style:none}
.adv-list li{display:flex;align-items:center;gap:8px;font-size:7.8px;letter-spacing:.4px;height:27px;white-space:nowrap}
.adv-list svg{width:14px;height:14px;flex:none}
.tool-photo{left:231px;top:0;width:269px;height:252px;background:linear-gradient(160deg,#3a4b6e 0%,#8a6a55 45%,#5e6a68 100%)}
.tile-photo{left:16px;top:173px;width:195px;height:92px;background:linear-gradient(180deg,#4f86c9 0%,#b9c2c8 45%,#707478 100%)}
.testi-tab{left:76px;top:268px;width:348px;height:40px;background:var(--maroon);border-radius:20px 20px 0 0}
.testi-head{left:0;top:276px;width:500px;height:38px;background:var(--maroon);border-radius:26px 26px 0 0}
.testi-title{left:0;top:283px;width:500px;text-align:center;color:var(--paper);font-family:"Montserrat",sans-serif;font-size:11.5px;letter-spacing:1px}
.testi-title b{font-weight:700}
.testi-body{left:0;top:300px;width:500px;height:282px;background:var(--paper)}
.review{width:205px;height:115px;border:1.5px solid var(--maroon);border-top:none;border-radius:0 0 4px 4px;text-align:center;font-family:"Montserrat",sans-serif}
.review::before{content:"";position:absolute;left:-1.5px;right:-1.5px;top:0;height:14px;border:1.5px solid var(--maroon);border-bottom:none;border-radius:16px 16px 0 0}
.stars{position:absolute;left:55px;top:-8px;width:95px;background:var(--paper);border:1.5px solid var(--maroon);border-top:none;color:var(--gold);font-size:14px;line-height:18px;letter-spacing:1px}
.review p{position:absolute;left:10px;right:10px;top:26px;font-size:8.4px;line-height:1.3;color:var(--maroon)}
.review .rule{position:absolute;left:70px;width:65px;top:84px;height:1px;background:var(--maroon)}
.review .who{position:absolute;left:0;right:0;top:92px;font-size:9.5px;font-weight:700;color:var(--ink)}
.r1{left:31px;top:309px}.r2{left:264px;top:309px}.r3{left:31px;top:444px}.r4{left:264px;top:444px}
.r3 p,.r4 p{top:30px}
.back-footer{left:0;top:582px;width:500px;height:66px;background:var(--maroon-deep);color:var(--paper)}
.back-cta{left:0;top:9px;width:390px;text-align:center;font-family:"Montserrat",sans-serif;font-size:11px}
.back-cta b{font-weight:700}
.back-rule{left:62px;top:28px;width:270px;height:1px;background:rgba(255,255,255,.6)}
.back-line{left:16px;top:40px;font-family:"Montserrat",sans-serif;font-size:8.5px;letter-spacing:1.5px;display:flex;gap:10px;align-items:center;white-space:nowrap}
.back-line svg{width:11px;height:11px;vertical-align:-1px;margin-right:5px}
.back-creds{left:408px;top:8px;width:88px;font-family:"Montserrat",sans-serif;font-size:7.5px;font-weight:600;letter-spacing:1px;line-height:1.25}
.vsep{width:1px;height:14px;background:rgba(255,255,255,.6)}
</style>
</head>
<body>

<section class="flyer flyer--front">
  <div class="abs hero-photo" role="img" aria-label="Roofer in hard hat and safety vest laying tiles on a roof"></div>
  <div class="abs logo-oval"><span class="logo-name">Gable Crest Builders Inc.</span></div>

  <div class="abs title-panel">
    <div class="title-main">GABLE CREST'S</div>
    <div class="title-sub">REMODELING</div>
    <div class="slogan">WHERE CRAFTSMEN REACH THE SUMMIT</div>
  </div>

  <div class="abs bar why-bar">WHY CHOOSE US</div>
  <p class="abs why-text">At GCB, we constantly take advantage of the vast amount of available roofing industry training, and we provide our clients with the best client experience, and the highest quality and most efficient roofing systems.</p>

  <div class="abs divider"></div>
  <div class="abs bar services-bar">OUR SERVICES</div>
  <ul class="abs services">
    <li><svg viewBox="0 0 18 18"><circle cx="9" cy="9" r="9" fill="#5a0b1e"/><path d="M4 11 9 6l5 5" stroke="#fff" stroke-width="1.6" fill="none"/></svg>Residential Roofing</li>
    <li><svg viewBox="0 0 18 18"><circle cx="9" cy="9" r="9" fill="#5a0b1e"/><path d="M4 12h10L11 6H7z" fill="#fff"/></svg>Commercial Roofing</li>
    <li><svg viewBox="0 0 18 18"><circle cx="9" cy="9" r="9" fill="#5a0b1e"/><path d="M4.5 9 9 5l4.5 4v4.5h-9z" fill="#fff"/></svg>Residential Exterior</li>
    <li><svg viewBox="0 0 18 18"><circle cx="9" cy="9" r="9" fill="#5a0b1e"/><path d="M9 4c2 3 3 4.5 3 6a3 3 0 0 1-6 0c0-1.5 1-3 3-6z" fill="#fff"/></svg>Roof leak repair</li>
    <li><svg viewBox="0 0 18 18"><circle cx="9" cy="9" r="9" fill="#5a0b1e"/><path d="M5 13 13 5M5 5l8 8" stroke="#fff" stroke-width="1.6"/></svg>Roof Maintenance</li>
    <li><svg viewBox="0 0 18 18"><circle cx="9" cy="9" r="9" fill="#5a0b1e"/><path d="M5 12l3-3 2 2 3-5" stroke="#fff" stroke-width="1.6" fill="none"/></svg>Specialty Roofing</li>
  </ul>

  <div class="abs about">
    <h2>ABOUT US</h2>
    <p>Gable Crest Builders is your one-stop shop for all your storm damage restoration needs. Our seasoned professionals use time-tested processes to restore your home after a storm, eliminating the hassles and headaches of working with multiple companies. Whether you need a roof replaced, or need exterior/interior damage repaired, you can trust Gable Crest Builders to complete your projects.</p>
    <p>We have learned over the years what our clients want. While each client and their project has its own unique attributes, the overall desire of each seem to be same... Excellence. So that's what we provide! From the initial visit to final inspection and all the details in between. We have worked diligently to ensure that our team and implemented systems are living up to that standard!</p>
  </div>

  <div class="abs footer">
    <div class="abs footer-cta">For More Information <b>CONTACT US</b></div>
    <div class="abs footer-rule"></div>
    <div class="abs footer-line">
      <span><svg viewBox="0 0 12 12"><path d="M2.5 1 4.5 1 5.3 3.6 4 4.6C4.6 6 6 7.4 7.4 8L8.4 6.7 11 7.5V9.5C11 10.3 10.3 11 9.5 11 5 11 1 7 1 2.5 1 1.7 1.7 1 2.5 1z" fill="#fff"/></svg>(555)382-6047</span>
      <span>www.gablecrestbuilding.example</span>
    </div>
    <div class="abs creds">LICENSED<br>BONDED<br>INSURED<span class="badge"></span><div class="social">Chatter web</div></div>
  </div>
</section>

<section class="flyer flyer--back">
  <div class="abs tool-photo" role="img" aria-label="Hands hammering a nail into roof shingles"></div>
  <div class="abs adv-box">
    <div class="adv-title">OUR ADVANTAGES</div>
    <ul class="adv-list">
      <li><svg viewBox="0 0 14 14"><rect x="1" y="2" width="11" height="11" fill="none" stroke="#fff" stroke-width="1.4"/><path d="M3.5 7.5 6 10l7-8" stroke="#fff" stroke-width="1.8" fill="none"/></svg>NO DOWN PAYMENTS</li>
      <li><svg viewBox="0 0 14 14"><rect x="1" y="2" width="11" height="11" fill="none" stroke="#fff" stroke-width="1.4"/><path d="M3.5 7.5 6 10l7-8" stroke="#fff" stroke-width="1.8" fill="none"/></svg>LICENSED BONDED &amp; INSURED</li>
      <li><svg viewBox="0 0 14 14"><rect x="1" y="2" width="11" height="11" fill="none" stroke="#fff" stroke-width="1.4"/><path d="M3.5 7.5 6 10l7-8" stroke="#fff" stroke-width="1.8" fill="none"/></svg>FREE ESTIMATED &amp; INSPECTIONS</li>
      <li><svg viewBox="0 0 14 14"><rect x="1" y="2" width="11" height="11" fill="none" stroke="#fff" stroke-width="1.4"/><path d="M3.5 7.5 6 10l7-8" stroke="#fff" stroke-width="1.8" fill="none"/></svg>LOCAL AND FAMILY OWNED</li>
    </ul>
  </div>
  <div class="abs tile-photo" role="img" aria-label="Grey clay roof tiles under a blue sky"></div>

  <div class="abs testi-tab"></div>
  <div class="abs testi-head"></div>
  <div class="abs testi-title">WHAT PEOPLE SAY <b>TESTIMONIALS</b></div>
  <div class="abs testi-body"></div>

  <div class="abs review r1"><span class="stars">★★★★★</span><p>Gable Crest Builders the best locally-owned &amp; exceptionally operated. They are a mazing to work with &amp; do the job right first time. You won't be disappointed!</p><span class="rule"></span><span class="who">Dale</span></div>
  <div class="abs review r2"><span class="stars">★★★★★</span><p>Great Company My hasband and I were very happy with this services. Our stimator was awesome to work With. The process was was very easy and Gable Crest Builders was realy Professional.</p><span class="rule"></span><span class="who">MARLA</span></div>
  <div class="abs review r3"><span class="stars">★★★★★</span><p>Fast and friendly owen went above and beyond to make our experience with Gable Crest Builders adream. They were a mazing and highly recommend them!</p><span class="rule"></span><span class="who">PETE</span></div>
  <div class="abs review r4"><span class="stars">★★★★★</span><p>Gable Crest Builders did a great job with our roof replacement everyone was very friendly and helpful and the quality of work was excellent.</p><span class="rule"></span><span class="who">WALTER</span></div>

  <div class="abs back-footer">
    <div class="abs back-cta">For More Information <b>CONTACT US</b></div>
    <div class="abs back-rule"></div>
    <div class="abs back-line">
      <span><svg viewBox="0 0 12 12"><path d="M2.5 1 4.5 1 5.3 3.6 4 4.6C4.6 6 6 7.4 7.4 8L8.4 6.7 11 7.5V9.5C11 10.3 10.3 11 9.5 11 5 11 1 7 1 2.5 1 1.7 1.7 1 2.5 1z" fill="#fff"/></svg>(555)382-6047</span>
      <span class="vsep"></span>
      <span>WWW.GABLECRESTBUILDING.EXAMPLE</span>
    </div>
    <div class="abs back-creds">LICENSED<br>BONDED<br>INSURED<span class="badge"></span><div class="social">Chatter web</div></div>
  </div>
</section>

</body>
</html>
```